Website Landing Page for Brightfall Systems

Create a custom designed website landing page for our business. Looking for a professional upscale design that incorporates our logo and logo colors into the theme. I want a standard fixed frame website, not a constant scrolling format that seems to be the trend. To start with I'm looking for more of the graphic design part, maybe a concept or theme, I don't expect to see a finished project. Not interested in generic templates or layouts.

The name of our company is Brightfall Systems and I've attached our logo below. I'd like to have the web page have the same look and feel of our logo, as well as the colors. Our company, Brightfall Systems does system design, installation, and programming, of residential and commercial Audio/Video and Automation systems. We do home theaters, lighting and building automation, video conferencing systems, security camera installations, conference rooms, projectors, distributed audio systems, and similar Technology projects. This will be a professional services/informational website. We will not sell products on this website. This website will be used to advertise our company and communicate our services to prospective customers. Having a well designed, professional and clean website is one way we want to distinguish our company from the competition.

Here are some examples of what I consider a professional well designed website
http://www.qorlamstudio.com/Work/

Last year we had our tradlo store designed (with PixelMarket) and I'm really happy with the way it turned out. You can see it at www.HolvenGearDepot.com I consider this to be a great design and looking for the same level of quality with this new website. However, do not copy or use any part of this design in this new project. This tradlo store is completely separate from our other company Brightfall Systems. I only mention this tradlo store an an example of good work.

Reason: Still going through designs.

Reason: Still working on project and have not had time to review all designs and request revisions.

Reason: Sill going through designs and requesting revisions

Reason: still going through all the submissions we received.

Target Market(s)

People interested in Audio/Video, home theaters, home automation. We do sales, system design, and programming. We typically work on larger projects with both residential and commercial customers.

Industry/Entity Type

Business

Number of Pages Required

1 page

Requirements
Must have
• Great design elements. Please use a white background. I think white goes well with our logo colors.

```html
<!DOCTYPE html>
<html lang="en">
<head>
<meta charset="utf-8">
<title>Brightfall Systems</title>
<link href="https://fonts.googleapis.com/css2?family=Roboto:wght@400;500;700&family=Oswald:wght@600&display=swap" rel="stylesheet">
<style>
:root{
  --blue:#3f7fc4;
  --navy:#0d4d8f;
  --sky:#35aee0;
  --green:#5cb845;
  --green-dark:#3f9a2c;
  --grey-bg:#ececec;
  --ink:#333;
  --nav-ink:#4a4a4a;
}
*{box-sizing:border-box;margin:0;padding:0}
html,body{width:786px;height:1200px;overflow:hidden;background:#fff;font-family:Roboto,Arial,sans-serif;color:var(--ink)}
.page{position:relative;width:786px;height:1200px}
.abs{position:absolute}

/* header */
.brand{left:28px;top:13px;display:flex;align-items:center;gap:10px}
.brand-mark{width:46px;height:46px;border-radius:50%;border:4px solid var(--sky)}
.brand-name{font-size:15px;font-weight:500;color:var(--sky);line-height:17px;letter-spacing:.5px}
.consult{left:254px;top:29px;font-size:11.5px;font-weight:500;color:var(--navy);display:flex;align-items:center;gap:5px}
.consult .num{font-size:14px;font-weight:400;color:#444;margin-left:2px}
.social{right:26px;top:27px;display:flex;gap:6px}
.social span{width:20px;height:20px;border:1.6px solid var(--navy);border-radius:50%}

/* nav */
.nav{left:29px;top:75px;width:729px;height:32px;background:#fff;border-radius:16px;box-shadow:0 1px 4px rgba(0,0,0,.25);display:flex;z-index:3;overflow:hidden}
.nav a{font-size:11.5px;color:var(--nav-ink);text-decoration:none;display:flex;align-items:center;justify-content:center;flex:1 1 auto;padding:0 12px;border-right:1px solid #ddd}
.nav a.active{background:var(--navy);color:#fff;flex:0 0 66px;padding:0}
.nav .search{flex:0 0 34px;background:var(--navy);display:flex;align-items:center;justify-content:center}

/* hero */
.hero-photo{left:0;top:90px;width:786px;height:293px;background:linear-gradient(90deg,#b99a6a 0%,#e6d7bb 12%,#f4ede0 25%,#2f6a3a 40%,#4f8a44 50%,#2c5d34 62%,#efe6d5 76%,#e3d3b4 88%,#b59468 100%)}
.hero-shade{left:0;top:90px;width:786px;height:293px;background:rgba(0,0,0,.18)}
.hero-title{left:0;top:175px;width:786px;text-align:center;font-family:Oswald,sans-serif;font-weight:600;font-size:60px;line-height:70px;color:#fff;letter-spacing:1px;text-shadow:0 2px 6px rgba(0,0,0,.5)}
.hero-sub{left:0;top:251px;width:786px;text-align:center;font-size:18px;color:#fff;text-shadow:0 1px 4px rgba(0,0,0,.6)}
.btn-read{left:356px;top:290px;width:78px;height:25px;border-radius:13px;background:var(--navy);border:1.5px solid #fff;color:#fff;font-size:11.5px;display:flex;align-items:center;justify-content:center}
.hero-arrow{top:190px}

/* section headings */
.sec-title{left:0;width:786px;text-align:center}
.divider{left:356px;width:75px;height:10px}

/* service cards */
.card{width:231px;height:117px;background:linear-gradient(#36afe0,#3f82c8);color:#fff;text-align:center}
.card.raised{box-shadow:0 3px 8px rgba(0,0,0,.35)}
.card h3{margin-top:38px;font-size:12.5px;font-weight:500;letter-spacing:.2px}
.card p{margin:6px auto 0;width:192px;font-size:9.5px;line-height:13.6px;opacity:.95}
.card .icon{position:absolute;left:91px;top:-27px;width:50px;height:50px;border-radius:50%;background:#fff;border:2px solid #777;display:flex;align-items:center;justify-content:center}
.card .icon.on{background:var(--blue);border-color:#fff;box-shadow:0 0 0 2px var(--blue)}
.card .more{position:absolute;left:106px;bottom:-9px;width:19px;height:19px;border-radius:50%;background:var(--blue);border:1.5px solid #fff;display:flex;align-items:center;justify-content:center}

/* about */
.about{left:0;top:795px;width:786px;height:209px;background:var(--grey-bg)}
.about-text{left:29px;top:866px;width:732px;text-align:center;font-size:11.5px;line-height:18.7px;color:#333}
.about-more{left:366px;top:950px;width:22px;height:22px;border-radius:50%;background:var(--blue);display:flex;align-items:center;justify-content:center}

/* contact */
.contact{left:0;top:1004px;width:786px;height:158px;background:var(--blue);color:#fff}
.contact h4{position:absolute;font-size:12px;font-weight:500}
.field{position:absolute;background:#fff;border-radius:5px;font-size:9px;color:#666;padding:9px 12px}
.submit{position:absolute;left:375px;top:77px;width:66px;height:62px;border-radius:4px;background:linear-gradient(135deg,var(--green),var(--green-dark));color:#fff;font-size:11px;font-weight:700;display:flex;align-items:center;justify-content:center}
.info{position:absolute;left:568px;display:flex;gap:7px;font-size:9.8px;line-height:12.4px}

/* footer */
.footer{left:0;top:1162px;width:786px;height:38px;background:var(--green);color:#fff;font-size:10px;display:flex;align-items:center;justify-content:space-between;padding:0 28px}
.footer .home{color:var(--navy)}
</style>
</head>
<body>
<div class="page">

  <div class="abs hero-photo" role="img" aria-label="Living room home theater with a large wall screen showing a waterfall, speakers and a plant"></div>
  <div class="abs hero-shade"></div>

  <div class="abs brand">
    <span class="brand-mark"></span>
    <span class="brand-name">BRIGHTFALL<br>SYSTEMS</span>
  </div>

  <div class="abs consult">CALL FOR A FREE CONSULTATION
    <svg width="20" height="20" viewBox="0 0 20 20"><circle cx="10" cy="10" r="10" fill="#0d4d8f"/><path d="M7 5.5c.6-.3 1 0 1.3.5l.8 1.6c.2.5 0 .9-.4 1.2l-.5.4c.5 1.2 1.3 2 2.4 2.5l.4-.5c.3-.4.8-.5 1.2-.3l1.6.9c.4.3.6.8.3 1.3-.6 1.2-1.8 1.6-3 1.1C8.7 13.3 6.8 11.4 6 9 5.6 7.5 6 6.2 7 5.5z" fill="#fff"/></svg>
    <span class="num">123 456 789</span>
  </div>

  <div class="abs social" aria-label="Social links"><span></span><span></span><span></span><span></span><span></span></div>

  <nav class="abs nav">
    <a class="active">HOME</a><a>ABOUT US</a><a>PRODUCTS</a><a>SYSTEMS</a><a>COMMERCIAL</a><a>RESIDENTIAL</a><a>GALLERY</a><a style="border-right:0">CONTACT US</a>
    <span class="search"><svg width="14" height="14" viewBox="0 0 14 14"><circle cx="8" cy="6" r="4.2" fill="none" stroke="#fff" stroke-width="1.8"/><path d="M5 9L1.5 12.5" stroke="#fff" stroke-width="1.8" stroke-linecap="round"/></svg></span>
  </nav>

  <h1 class="abs hero-title">HOME THEATERS</h1>
  <p class="abs hero-sub">Lorem ipsum dolor sit amet consect Adipiscing elituspendiss</p>
  <div class="abs btn-read">Read More</div>
  <svg class="abs hero-arrow" style="left:0" width="30" height="92" viewBox="0 0 30 92"><path d="M27 2L3 46l24 44" fill="none" stroke="#fff" stroke-width="3"/></svg>
  <svg class="abs hero-arrow" style="left:748px" width="32" height="92" viewBox="0 0 32 92"><path d="M3 2l26 44L3 90" fill="none" stroke="#fff" stroke-width="3"/></svg>

  <div class="abs sec-title" style="top:413px;font-size:14px;font-weight:500">WHAT WE DO</div>
  <svg class="abs divider" style="top:431px" viewBox="0 0 75 10"><path d="M0 5h30M45 5h30" stroke="#5cb845" stroke-width="2.5"/><circle cx="37.5" cy="5" r="3" fill="#0d4d8f"/></svg>

  <!-- row 1 -->
  <div class="abs card raised" style="left:29px;top:472px">
    <span class="icon on"><svg width="26" height="22" viewBox="0 0 26 22"><rect x="1.5" y="1.5" width="23" height="15" rx="1.5" fill="none" stroke="#fff" stroke-width="2"/><path d="M8 20h10M13 17v3" stroke="#fff" stroke-width="2"/></svg></span>
    <h3>HOME THEATER</h3>
    <p>Lorem ipsum dolor sit amet, consectetur adiscing placerat, orci eget pretium lacinia arcu nulla .suipit erosd consequat metus</p>
    <span class="more"><svg width="8" height="10" viewBox="0 0 8 10"><path d="M2 1l4 4-4 4" fill="none" stroke="#fff" stroke-width="2"/></svg></span>
  </div>
  <div class="abs card" style="left:279px;top:472px">
    <span class="icon"><svg width="20" height="26" viewBox="0 0 20 26"><path d="M10 1a8 8 0 0 0-4.5 14.6V19h9v-3.4A8 8 0 0 0 10 1z" fill="#555"/><rect x="6" y="20.5" width="8" height="2" fill="#555"/><rect x="7.5" y="23.5" width="5" height="2" fill="#555"/></svg></span>
    <h3>LIGHTING &amp; BUILDING AUTOMATION</h3>
    <p>Lorem ipsum dolor sit amet, consectetur adiscing placerat, orci eget pretium lacinia arcu nulla .suipit erosd consequat metus</p>
    <span class="more"><svg width="8" height="10" viewBox="0 0 8 10"><path d="M2 1l4 4-4 4" fill="none" stroke="#fff" stroke-width="2"/></svg></span>
  </div>
  <div class="abs card" style="left:529px;top:472px">
    <span class="icon"><svg width="26" height="26" viewBox="0 0 26 26"><circle cx="13" cy="11" r="9" fill="none" stroke="#555" stroke-width="1.8"/><circle cx="13" cy="11" r="4" fill="none" stroke="#555" stroke-width="1.8"/><path d="M5 24h16l-3-4H8z" fill="none" stroke="#555" stroke-width="1.8"/></svg></span>
    <h3>VIDEO CONFERENCING SYSTEMS</h3>
    <p>Lorem ipsum dolor sit amet, consectetur adiscing placerat, orci eget pretium lacinia arcu nulla .suipit erosd consequat metus</p>
    <span class="more"><svg width="8" height="10" viewBox="0 0 8 10"><path d="M2 1l4 4-4 4" fill="none" stroke="#fff" stroke-width="2"/></svg></span>
  </div>

  <!-- row 2 -->
  <div class="abs card" style="left:29px;top:638px">
    <span class="icon"><svg width="30" height="22" viewBox="0 0 30 22"><rect x="1" y="3" width="7" height="16" fill="none" stroke="#555" stroke-width="1.6"/><rect x="22" y="3" width="7" height="16" fill="none" stroke="#555" stroke-width="1.6"/><rect x="9" y="9" width="12" height="8" fill="#555"/><circle cx="4.5" cy="14" r="2" fill="#555"/><circle cx="25.5" cy="14" r="2" fill="#555"/></svg></span>
    <h3>DISTRIBUTED AUDIO SYSTEMS</h3>
    <p>Lorem ipsum dolor sit amet, consectetur adiscing placerat, orci eget pretium lacinia arcu nulla .suipit erosd consequat metus</p>
    <span class="more"><svg width="8" height="10" viewBox="0 0 8 10"><path d="M2 1l4 4-4 4" fill="none" stroke="#fff" stroke-width="2"/></svg></span>
  </div>
  <div class="abs card" style="left:279px;top:638px">
    <span class="icon"><svg width="30" height="18" viewBox="0 0 30 18"><rect x="1" y="2" width="28" height="13" rx="5" fill="none" stroke="#555" stroke-width="2"/><circle cx="20" cy="8.5" r="4" fill="none" stroke="#555" stroke-width="2"/><path d="M6 6v5M9 6v5M12 6v5" stroke="#555" stroke-width="1.6"/></svg></span>
    <h3>CONFERENCE ROOMS PROJECTORS</h3>
    <p>Lorem ipsum dolor sit amet, consectetur adiscing placerat, orci eget pretium lacinia arcu nulla .suipit erosd consequat metus</p>
    <span class="more"><svg width="8" height="10" viewBox="0 0 8 10"><path d="M2 1l4 4-4 4" fill="none" stroke="#fff" stroke-width="2"/></svg></span>
  </div>
  <div class="abs card" style="left:529px;top:638px">
    <span class="icon"><svg width="26" height="28" viewBox="0 0 26 28"><rect x="4" y="3" width="18" height="9" rx="1" transform="rotate(-20 13 7)" fill="none" stroke="#555" stroke-width="1.8"/><path d="M11 14v8M7 26h8M11 22l-3 4" fill="none" stroke="#555" stroke-width="1.8"/></svg></span>
    <h3>SECURITY CAMERA INSTALLATIONS</h3>
    <p>Lorem ipsum dolor sit amet, consectetur adiscing placerat, orci eget pretium lacinia arcu nulla .suipit erosd consequat metus</p>
    <span class="more"><svg width="8" height="10" viewBox="0 0 8 10"><path d="M2 1l4 4-4 4" fill="none" stroke="#fff" stroke-width="2"/></svg></span>
  </div>

  <!-- about -->
  <div class="abs about"></div>
  <div class="abs sec-title" style="top:824px;font-size:19px">ABOUT US</div>
  <svg class="abs divider" style="top:853px" viewBox="0 0 75 10"><path d="M0 5h30M45 5h30" stroke="#5cb845" stroke-width="2.5"/><circle cx="37.5" cy="5" r="3" fill="#0d4d8f"/></svg>
  <p class="abs about-text">Lorem ipsum dolor sit amet consectetur adipiscing elittiam pellentesque felis ut aliquet pharetra justo ante pharetra mauris ac eleifend metus orci at mauris. Aliquam sed sagittis nisi. Interdum et malesuada fames ac ante ipsum primis in faucibus. Nulla tempor eleifend odio accumsan lobortised auctor sapien metus, id dapibus felis pharetra eu. Phasellus in nisi id nisi vulputate tincidunt vel vitae purus. Accumsa volutpat vel tortor-liquam sodales lacus ac velit venenatis, in fermentum orci consequat In pulvinar vitae ipsum nec tempus</p>
  <span class="abs about-more"><svg width="9" height="12" viewBox="0 0 9 12"><path d="M2 1l5 5-5 5" fill="none" stroke="#fff" stroke-width="2.2"/></svg></span>

  <!-- contact -->
  <section class="abs contact">
    <h4 style="left:29px;top:14px">CONTACT US</h4>
    <div class="field" style="left:29px;top:39px;width:202px;height:28px">Your Name:</div>
    <div class="field" style="left:240px;top:39px;width:201px;height:28px">Email:</div>
    <div class="field" style="left:29px;top:77px;width:336px;height:62px">Comments:</div>
    <div class="submit">SUBMIT</div>

    <h4 style="left:567px;top:14px">VISIT TO BRIGHTFALL SYSTEMS</h4>
    <div class="info" style="top:37px">
      <svg width="18" height="18" viewBox="0 0 18 18"><path d="M8 1h2v16H8zM3 4h12l2 2-2 2H3zM2 9h5v3H2L1 10.5z" fill="#fff"/></svg>
      <span>Lorem ipsum streat 9, Level 2<br>Pellentesq Fringilla USA 2216</span>
    </div>
    <div class="info" style="top:82px">
      <svg width="16" height="18" viewBox="0 0 16 18"><path d="M3 2c1-.5 1.6 0 2 .8l1.2 2.4c.3.7 0 1.3-.6 1.7l-.6.5c.7 2 1.8 3.5 3.4 4.6l.6-.6c.5-.5 1.2-.6 1.8-.2l2 1.4c.6.5.7 1.2.2 1.8-1 1.5-2.6 1.8-4.2 1C5.2 14 3 10.5 2 7 1.5 5 1.9 3 3 2z" fill="none" stroke="#fff" stroke-width="1.4"/></svg>
      <span>123 456 7890</span>
    </div>
    <div class="info" style="top:126px">
      <svg width="18" height="13" viewBox="0 0 18 13"><rect x=".8" y=".8" width="16.4" height="11.4" fill="none" stroke="#fff" stroke-width="1.4"/><path d="M1 1l8 6 8-6M1 12l6-5M17 12l-6-5" fill="none" stroke="#fff" stroke-width="1.4"/></svg>
      <span>info@brightfallsystems.com</span>
    </div>
  </section>

  <footer class="abs footer">
    <span><span class="home">Home</span> &nbsp;/&nbsp; About Us &nbsp;/&nbsp; Prodcuts &nbsp;/&nbsp; Systems &nbsp;/&nbsp; Commercial &nbsp;/&nbsp; Residential &nbsp;/&nbsp; Gallery &nbsp;/&nbsp; Contact Us</span>
    <span>© 2017 Brightfall Systems. &nbsp;All right sserverd</span>
  </footer>

</div>
</body>
</html>
```